Camp Brookhaven 2018

We need a postcard design to advertise our summer programs. We are a Christian camp with day camp and overnight camps.

Target Market(s)

parents of elementary age kids

Industry/Entity Type

Christian

Colors
ec1f27
f37122
faa54b
fbee3d
f78f20
f04a50
fbed22
fbee3e

Requirements
Must have
• Day Camp 2018 "Shine Bright Daily"
• June 25 - August 24
• $135 per week
• Mon-Fri 8 am to 4 pm. Open to all kids entering grades 1 to 8. Day camp is chock full of activities like swimming, rock wall, archery, sports, crafts, air rifles and much more! Daily lunch and snack included. Before and after-care available at an extra rate.
• Register and pay in full by April 1st, save $270!
• Overnight Camp 2018
• July 15 - 21 & July 22 - 28
• $330 per week
• Open to all kids ages 8 to 14. Spend the week making new friends, sleeping in cabins, climbing the rock wall and swimming at the beach! Our guest speakers will lead twice daily chapel sessions that will challenge campers to grow in their faith.
• 41 Maple Crest Rd. Barrington, NH 03917
• 603-418-2956
• www.brookhavencamp.org
Nice to have
• bright and colorful

```html
<!DOCTYPE html>
<html lang="en">
<head>
<meta charset="utf-8">
<title>Camp Brookhaven 2018 Postcard</title>
<link rel="stylesheet" href="https://fonts.googleapis.com/css2?family=Barlow:wght@200;700;800&family=Catamaran:wght@400;600&display=swap">
<style>
  :root {
    --orange: #f07f12;
    --white: #ffffff;
    --rule: rgba(255,255,255,.85);
    --brand-red: #b52a1c;
    --stage: #ecebe8;
    --photo-a: #c9a98a;
    --photo-b: #8fb86a;
    --photo-c: #c25aa8;
  }
  * { box-sizing: border-box; margin: 0; padding: 0; }
  html, body { width: 1200px; height: 600px; overflow: hidden; }
  body {
    background: var(--stage);
    font-family: "Catamaran", sans-serif;
    position: relative;
  }
  .postcard {
    position: absolute;
    top: 120px;
    width: 540px;
    height: 360px;
    overflow: hidden;
    box-shadow: 0 4px 14px rgba(0,0,0,.18);
  }
  .postcard--front { left: 40px; background: var(--orange); }
  .postcard--back { left: 620px; background: var(--white); }

  /* Front */
  .front-photo { position: absolute; inset: 0; }
  .front-headline {
    position: absolute;
    left: 18px;
    top: 10px;
    font-family: "Barlow", sans-serif;
    color: var(--white);
    font-size: 71px;
    line-height: 64px;
    text-transform: uppercase;
    white-space: nowrap;
  }
  .front-headline .thin { font-weight: 200; display: block; letter-spacing: 3px; }
  .front-headline .bold { font-weight: 800; display: block; letter-spacing: 0; }
  .brand {
    position: absolute;
    display: flex;
    align-items: center;
    gap: 5px;
    font-weight: 600;
    font-size: 13px;
    line-height: 1;
    color: var(--brand-red);
    white-space: nowrap;
  }
  .brand-dot { width: 9px; height: 9px; border-radius: 50%; background: var(--brand-red); }
  .postcard--front .brand { left: 15px; top: 324px; }

  /* Back */
  .back-panel {
    position: absolute;
    left: 0; top: 0;
    width: 540px;
    height: 313px;
    background: var(--orange);
    color: var(--white);
  }
  .rule-v {
    position: absolute;
    left: 270px; top: 17px;
    width: 1px; height: 213px;
    background: var(--rule);
  }
  .rule-h {
    position: absolute;
    left: 30px; top: 166px;
    width: 475px; height: 1px;
    background: var(--rule);
  }
  .program {
    position: absolute;
    top: 13px;
    text-align: center;
  }
  .program--day { left: 42px; width: 216px; }
  .program--overnight { left: 276px; width: 226px; }
  .program-title {
    font-family: "Barlow", sans-serif;
    font-weight: 700;
    font-size: 13.5px;
    line-height: 18px;
    height: 40px;
    text-transform: uppercase;
  }
  .program--overnight .program-title { padding-top: 9px; }
  .program-desc {
    font-size: 10.6px;
    line-height: 15.2px;
    height: 113px;
  }
  .program-details {
    padding-top: 3px;
    font-size: 10.6px;
    line-height: 16.5px;
  }
  .program-offer { text-decoration: underline; }
  .program-offer strong { font-weight: 600; }
  .contact {
    position: absolute;
    left: 0; right: 0;
    top: 247px;
    text-align: center;
    font-style: normal;
    font-size: 10.6px;
    line-height: 15.5px;
  }
  .postcard--back .brand { left: 50%; transform: translateX(-50%); top: 334px; }
</style>
</head>
<body>
  <section class="postcard postcard--front">
    <svg class="front-photo" width="540" height="360" viewBox="0 0 540 360" role="img" aria-label="Photo of smiling children in colourful swimsuits and goggles at summer camp">
      <defs>
        <linearGradient id="photoTone" x1="0" y1="0" x2="1" y2="1">
          <stop offset="0" stop-color="#c9a98a"/>
          <stop offset=".5" stop-color="#8fb86a"/>
          <stop offset="1" stop-color="#c25aa8"/>
        </linearGradient>
      </defs>
      <polygon points="463,0 540,0 540,360 98,360" fill="url(#photoTone)"/>
    </svg>
    <h1 class="front-headline">
      <span class="thin">Enjoy your</span>
      <span class="thin">childrens</span>
      <span class="bold">Happieness</span>
    </h1>
    <div class="brand"><span class="brand-dot"></span>Camp Brookhaven</div>
  </section>

  <section class="postcard postcard--back">
    <div class="back-panel">
      <span class="rule-v"></span>
      <span class="rule-h"></span>
      <article class="program program--day">
        <h2 class="program-title">Day Camp 2018<br>«Shine Bright Daily»</h2>
        <p class="program-desc">Mon-Fri 8 am to 4 pm. Open to all kids entering grades 1 to 8. Day camp is chock full of activities like swimming, rock wall, archery, sports, crafts, air rifles and much more! Daily lunch and snack included. Before and after-care available at an extra rate.</p>
        <p class="program-details">June 25 - August 24<br>$135 per week<br><span class="program-offer">Register and pay in full by April 1st, save <strong>$270</strong></span>!</p>
      </article>
      <article class="program program--overnight">
        <h2 class="program-title">Overnight Camp 2018</h2>
        <p class="program-desc">Open to all kids ages 8 to 14. Spend the week making new friends, sleeping in cabins, climbing the rock wall and swimming at the beach! Our guest speakers will lead twice daily chapel sessions that will challenge campers to grow in their faith.</p>
        <p class="program-details">July 15 - 21 &amp; July 22 - 28<br>$330 per week</p>
      </article>
      <address class="contact">41 Maple Crest Rd. Barrington, NH 03917<br>603-418-2956<br>www.brookhavencamp.org</address>
    </div>
    <div class="brand"><span class="brand-dot"></span>Camp Brookhaven</div>
  </section>
</body>
</html>
```